Business card design for a engineering company

I need a double sided business card design for my company "Verdmont Flow Solutions". The card will be used in Malaysia. Sleek and professional, with a little design flare to it.
Information to showcase:
1. Company logo
2. Name, title, phone, email address, website address
3. our products "Pumping technology, Valve & actuation, Air Moving Technology
Example:
Ravi Tanaka
Business manager
ravi.tanaka@verdmont-example.com
www.verdmont-example.com.my
- Pumping technology
- Valve & actuation
- Air moving technology
Target Market(s)
engineers, purchasing managers
Industry/Entity Type
Business
Contact Information for Business Card
Ravi Tanaka
Business manager
ravi.tanaka@verdmont-example.com
www.verdmont-example.com.my
- Pumping technology
- Valve & actuation
- Air moving technology
catch phrase : "Solving flow challenges, exceeding expectations"

```html
<!DOCTYPE html>
<html lang="en">
<head>
<meta charset="utf-8">
<title>Verdmont Flow Solutions – Business Card</title>
<link rel="stylesheet" href="https://fonts.googleapis.com/css2?family=Open+Sans:wght@300;400;600;700&display=swap">
<style>
  :root {
    --navy: #0b3344;
    --orange: #f39a1f;
    --ink: #3a3a3a;
    --paper: #ffffff;
    --backdrop: #e9e6e1;
  }
  * { box-sizing: border-box; margin: 0; padding: 0; }
  html, body {
    width: 1200px; height: 987px; overflow: hidden;
    background: var(--backdrop);
    font-family: "Open Sans", Arial, sans-serif;
  }
  .card {
    position: absolute; left: 293px;
    width: 615px; height: 350px;
    overflow: hidden;
  }
  .card-front { top: 131px; background: var(--paper); }
  .card-back { top: 506px; background: var(--navy); }

  .name-band {
    position: absolute; left: 0; top: 50px;
    width: 300px; height: 59px;
    background: var(--navy); color: #fff;
    padding: 7px 0 0 33px;
  }
  .person-name { font-size: 20px; font-weight: 700; letter-spacing: 0.5px; line-height: 24px; }
  .person-title { font-size: 16.5px; font-weight: 400; line-height: 21px; }

  .brand {
    position: absolute; left: 281px; top: 57px;
    display: flex; align-items: center; gap: 12px;
  }
  .brand-dot { flex: none; width: 44px; height: 44px; border-radius: 50%; background: var(--orange); }
  .brand-name { font-size: 18px; font-weight: 600; color: var(--navy); letter-spacing: 0.3px; white-space: nowrap; }

  .contact {
    position: absolute; left: 0; right: 0; top: 266px;
    text-align: center; color: var(--ink);
    font-size: 13.5px; line-height: 26px;
    white-space: nowrap;
  }
  .contact .bullet { font-size: 9px; vertical-align: 2px; padding: 0 3px; }

  .back-brand {
    position: absolute; left: 0; right: 0; top: 140px;
    display: flex; justify-content: center; align-items: center; gap: 16px;
  }
  .back-brand .brand-dot { width: 60px; height: 60px; }
  .back-brand .brand-name { color: #fff; font-size: 28px; }
  .tagline {
    position: absolute; left: 0; right: 0; top: 291px;
    text-align: center; color: #fff;
    font-size: 17px; font-weight: 300;
  }
</style>
</head>
<body>
  <section class="card card-front">
    <div class="name-band">
      <div class="person-name">RAVI TANAKA</div>
      <div class="person-title">Business manager</div>
    </div>
    <div class="brand">
      <span class="brand-dot"></span>
      <span class="brand-name">Verdmont Flow Solutions</span>
    </div>
    <div class="contact">
      <p>689 555 0142 | ravi.tanaka@verdmont-example.com | www.verdmont-example.com.my</p>
      <p>Pumping technology <span class="bullet">●</span> Valve &amp; actuation <span class="bullet">●</span> Air moving technology</p>
    </div>
  </section>

  <section class="card card-back">
    <div class="back-brand">
      <span class="brand-dot"></span>
      <span class="brand-name">Verdmont Flow Solutions</span>
    </div>
    <p class="tagline">Solving flow challenges, exceeding expectations</p>
  </section>
</body>
</html>
```